Brackenfield Prime Healthcare Needs a Business Card Design

We need a business card design for a company based in Shorewood IL called "Brackenfield Prime Healthcare". We provide an integrated medical model involving chiropractic, trigger point injections and other medical services in one location. I have attached our logo to this with the colors being in the puzzle design of the logo. We are looking for a great design that will WOW those around us but also be able to communicate our information easily

Industry/Entity Type

Medical

Contact Information for Business Card

This is a integrated Medical office featuring numerous services to clients in the office.

Requirements
Must have
• Logo

```html
<!DOCTYPE html>
<html lang="en">
<head>
<meta charset="utf-8">
<title>Brackenfield Prime Healthcare – Business Card</title>
<link href="https://fonts.googleapis.com/css2?family=Raleway:wght@500;600;700&display=swap" rel="stylesheet">
<style>
  :root {
    --backdrop: #3b3b3b;
    --card: #ffffff;
    --accent: #5fc6de;
    --ink: #333333;
    --brand: #3d6fb6;
  }
  * { margin: 0; padding: 0; box-sizing: border-box; }
  html, body { width: 1200px; height: 1000px; overflow: hidden; }
  body {
    position: relative;
    background: var(--backdrop);
    font-family: "Raleway", Arial, sans-serif;
    color: var(--ink);
  }
  .card {
    position: absolute;
    top: 172px;
    width: 386px;
    height: 660px;
    background: var(--card);
  }
  .card--front { left: 149px; }
  .card--back { left: 617px; width: 387px; }
  .card__bar {
    position: absolute;
    left: 59px;
    width: 268px;
    height: 17px;
    background: var(--accent);
  }
  .card__bar--top { top: 0; border-radius: 0 0 3px 3px; }
  .card__bar--bottom { bottom: 0; border-radius: 3px 3px 0 0; }

  .brand {
    position: absolute;
    top: 127px;
    left: 50px;
    width: 286px;
    height: 58px;
    display: flex;
    align-items: center;
    justify-content: center;
    gap: 10px;
  }
  .brand__mark {
    width: 30px; height: 30px;
    background: var(--accent);
    flex: none;
  }
  .brand__name {
    font-weight: 700;
    font-size: 17px;
    line-height: 1.15;
    color: var(--brand);
    letter-spacing: 0.3px;
  }

  .centered { position: absolute; left: 0; width: 100%; text-align: center; }
  .person__name { top: 260px; font-size: 21px; font-weight: 700; color: var(--accent); letter-spacing: 0.3px; }
  .person__title { top: 290px; font-size: 16px; font-weight: 600; }
  .contact { top: 363px; font-size: 17px; font-weight: 600; line-height: 28px; }
  .contact__label { color: var(--accent); font-weight: 700; }
  .office { top: 491px; font-size: 17px; font-weight: 600; line-height: 28px; }
  .office__name { color: var(--accent); font-weight: 700; }

  .services { position: absolute; top: 154px; left: 5px; width: 100%; }
  .service { text-align: center; height: 95px; }
  .service__icon { display: block; margin: 0 auto 9px; width: 32px; height: 32px; }
  .service__label { font-size: 17px; font-weight: 600; }
</style>
</head>
<body>
  <section class="card card--front">
    <div class="card__bar card__bar--top"></div>
    <div class="brand">
      <span class="brand__mark"></span>
      <span class="brand__name">BRACKENFIELD PRIME<br>HEALTHCARE</span>
    </div>
    <p class="centered person__name">MARCUS ELLERY</p>
    <p class="centered person__title">Director, M.B.B.S.</p>
    <div class="centered contact">
      <p><span class="contact__label">P:</span> 815-555-0142</p>
      <p><span class="contact__label">E:</span> info@brackenfieldhealthcare.com</p>
      <p><span class="contact__label">W:</span> brackenfieldhealthcare.com</p>
    </div>
    <div class="centered office">
      <p class="office__name">BRACKENFIELD PRIME HEALTHCARE</p>
      <p>412 Alder Ridge Rd, Unit C</p>
      <p>Maplecrest, IL 60417</p>
    </div>
    <div class="card__bar card__bar--bottom"></div>
  </section>

  <section class="card card--back">
    <div class="card__bar card__bar--top"></div>
    <div class="services">
      <div class="service">
        <svg class="service__icon" viewBox="0 0 32 32" role="img" aria-label="Therapist treating a patient icon"><rect width="32" height="32" rx="4" fill="var(--accent)"/></svg>
        <p class="service__label">Physical Rehabilitation</p>
      </div>
      <div class="service">
        <svg class="service__icon" viewBox="0 0 32 32" aria-hidden="true"><rect width="32" height="32" rx="4" fill="var(--accent)"/><rect x="7" y="10" width="18" height="14" rx="2" fill="#fff"/><rect x="12" y="7" width="8" height="4" rx="1" fill="none" stroke="#fff" stroke-width="2"/><rect x="14.5" y="12.5" width="3" height="9" fill="var(--accent)"/><rect x="11.5" y="15.5" width="9" height="3" fill="var(--accent)"/></svg>
        <p class="service__label">Medical Pain Relief</p>
      </div>
      <div class="service">
        <svg class="service__icon" viewBox="0 0 32 32" role="img" aria-label="Human body figure icon"><rect width="32" height="32" rx="4" fill="var(--accent)"/></svg>
        <p class="service__label">Chiropractic Care</p>
      </div>
      <div class="service">
        <svg class="service__icon" viewBox="0 0 32 32" aria-hidden="true"><rect width="32" height="32" rx="4" fill="var(--accent)"/><rect x="7" y="7" width="18" height="18" rx="4" fill="#fff"/><path d="M11 13 a5 4 0 0 1 10 0 z" fill="var(--accent)"/></svg>
        <p class="service__label">Weight Loss Programs</p>
      </div>
    </div>
    <div class="card__bar card__bar--bottom"></div>
  </section>
</body>
</html>
```